**URGENT // ENVIRONMENTAL // QUICK TURN AROUND**

We are looking for an A-Grade designer to work with longterm, starting with the successful design for our website & logo; Pelham Grove.

Pelham Grove is a business that focusses on grouping environmentally conscious people together and helping them get "bulk buy" discounts by purchasing large volumes together; solar, energy efficency, wind turbines, and the like.

The Logo and website must have a green feel, as we are here to protect the environment, whilst also helping our customers save money.

The website must also have a blog feature, allowing us to post and keep people up to date with the latest in the industry.

Target Market(s)

FAMILIES WITHIN REGIONAL AUSTRALIA WANTING TO EITHER SAVE MONEY ON ELECTRICITY BILLS, OR REDUCE CARBON EMISSIONS.

Industry/Entity Type

Solar Energy

Logo Text

PELHAM GROVE

Number of Pages Required

5+ page

Font styles to use
Serif
Sans Serif

Colors

Designer to choose colors to be used in the design.

Requirements
Must have
• 1.HOME PAGE
• 2.OUR SERVICES PAGE
• - RENEWABLE ENERGY
• - LIGHTING SYSTEMS
• - ENERGY ASSESSMENT
• - R.G.L.C SCHEME
• - ENERGY COMPARISON
• 4. BOOK AN APPOINTMENT
• 5. IN THE NEWS
• 6. SUBSCRIBE TO NEWSLETTER
• 7. CONTACT US
• MUST LOOK VERY PROFESSIONAL, WITH LOTS OF INFORMATION, IT CANNOT BE BARE AND SIMPLE.
• Can use www.marlowfieldtrading.com.au which is our other brand for copy and ideas - HOWEVER, THIS IS THE REASON WE ARE RE-BRANDING, AS THIS BRAND HAS COME UNDER FAR TOO MUCH CRITICISM FOR LACK OF INFORMATION AND LOOKING TO SIMPLE.
Nice to have
• BLOG FEATURE
Should not have
• ANYTHING THAT APPEARS NON-ENVIRONMENTALS

```html
<!DOCTYPE html>
<html lang="en">
<head>
<meta charset="utf-8">
<title>Careers – Pelham Grove</title>
<link href="https://fonts.googleapis.com/css2?family=Roboto+Condensed:wght@400;700&family=Roboto:wght@400;500;700&display=swap" rel="stylesheet">
<style>
:root{
  --ink:#1b2a20;
  --forest:#1f4d2c;
  --forest-deep:#173d22;
  --leaf:#2f8f3f;
  --text:#6a7069;
  --line:#e2e6e1;
  --band:#edf1ec;
  --lime:#cfe36a;
  --footer:#162219;
  --footer-text:#8e998f;
  --footer-line:#2c3a30;
  --footer-chip:#24332a;
  --white:#fff;
}
*{box-sizing:border-box;margin:0;padding:0}
html,body{width:1082px;height:1200px;overflow:hidden;background:var(--white)}
body{position:relative;font-family:"Roboto",sans-serif;color:var(--text);font-size:8.4px}
.abs{position:absolute}

.topbar{left:0;top:0;width:1082px;height:25px;background:var(--footer);color:#b9c3ba;font-size:7.6px}
.topbar .contact{left:211px;top:8px;display:flex;gap:10px;align-items:center}
.topbar .contact svg{vertical-align:-2px;margin-right:5px}
.topbar .socials{left:632px;top:0;display:flex;height:25px}
.topbar .socials span{width:25px;height:25px;border-left:1px solid var(--footer-line);display:flex;align-items:center;justify-content:center}
.topbar .socials i{width:5px;height:5px;background:#c3ccc4;border-radius:50%}
.topbar .search{left:757px;top:0;width:114px;height:25px;border-left:1px solid var(--footer-line);border-right:1px solid var(--footer-line);padding:9px 10px;color:#56625a;font-size:7px}
.topbar .search svg{position:absolute;right:9px;top:8px}

.header{left:0;top:25px;width:1082px;height:57px}
.logo{left:213px;top:19px;display:flex;align-items:center;gap:7px;font-weight:700;font-size:17px;color:var(--forest);letter-spacing:.6px}
.logo i{width:12px;height:12px;border-radius:50%;background:var(--leaf)}
.nav{left:472px;top:24px;display:flex;gap:21px;font-family:"Roboto Condensed",sans-serif;font-size:8.5px;color:var(--ink);letter-spacing:.4px}
.quote{left:792px;top:14px;width:79px;height:28px;background:var(--leaf);color:#fff;font-family:"Roboto Condensed",sans-serif;font-size:7.5px;letter-spacing:.4px;display:flex;align-items:center;justify-content:center}

.crumb{left:0;top:82px;width:1082px;height:33px;background:var(--band);font-size:8.2px;padding:12px 0 0 211px;color:#7b837c}
.crumb b{font-weight:400;color:var(--ink)}

.side-box{left:211px;top:161px;width:151px;height:200px;border:1px solid var(--forest)}
.side-box h3{background:var(--forest);color:#fff;font-family:"Roboto Condensed",sans-serif;font-size:10px;letter-spacing:.5px;height:30px;padding:10px 16px}
.side-box ul{list-style:none;margin-top:12px}
.side-box li{height:25px;padding:7px 16px;font-size:8.4px;color:var(--ink)}
.side-box li.current{background:#f1f4f0}
.brochure{left:211px;top:378px;width:151px;height:33px;background:var(--leaf);color:#fff;font-family:"Roboto Condensed",sans-serif;font-size:8.5px;letter-spacing:.4px;padding:12px 0 0 43px}
.brochure svg{position:absolute;left:13px;top:10px}
.testimonial{left:211px;top:429px;width:151px;height:155px;border:1px solid var(--forest);padding:16px 16px 0}
.testimonial h3{font-family:"Roboto Condensed",sans-serif;color:var(--forest);font-size:10px;letter-spacing:.3px;margin-bottom:10px}
.testimonial p{font-size:8.4px;line-height:13.6px;letter-spacing:.15px}
.author{left:227px;top:566px;width:124px;height:36px;background:#fff;display:flex;gap:8px;align-items:flex-start;padding-left:2px}
.avatar{width:34px;height:34px;background:linear-gradient(135deg,#e0b040,#c5562e 60%,#3f6a4a)}
.author b{display:block;font-family:"Roboto Condensed",sans-serif;color:var(--ink);font-size:8.4px;margin-top:5px}
.author small{font-size:6.8px;color:#8a928b;letter-spacing:.2px}

.intro{left:381px;top:161px;width:318px}
.intro h1{font-family:"Roboto Condensed",sans-serif;font-size:13.5px;color:var(--ink);font-weight:700;margin:0 0 10px}
.intro p{font-size:8.4px;line-height:13.6px;letter-spacing:.15px}
.cols{left:381px;top:276px;width:320px;display:flex;gap:16px}
.cols div{width:152px}
.cols h2{font-family:"Roboto Condensed",sans-serif;font-size:10px;color:var(--ink);margin-bottom:14px}
.cols p{font-size:8.4px;line-height:13.6px;letter-spacing:.15px}
.photo{left:718px;top:161px;width:153px;height:231px;background:linear-gradient(160deg,#dfe3e0 0%,#eef1ee 40%,#8fa394 72%,#2e4a36 100%)}

.acc-open{left:381px;top:426px;width:490px;height:100px;border:1px solid var(--line)}
.acc-open .head{background:var(--forest);height:28px;color:#fff;font-family:"Roboto Condensed",sans-serif;font-size:10px;font-weight:700;padding:8px 12px;position:relative}
.acc-open .head span{position:absolute;right:12px;top:6px;font-weight:400;font-size:12px}
.acc-open p{padding:9px 12px;font-size:8.4px;line-height:13.6px;letter-spacing:.2px}
.acc{left:381px;width:490px;height:28px;border:1px solid var(--line);font-family:"Roboto Condensed",sans-serif;font-size:10px;font-weight:700;color:var(--ink);padding:7px 11px}
.acc span{position:absolute;right:11px;top:5px;font-weight:400;font-size:12px}

.jobs{left:381px;top:633px;width:490px;border-collapse:collapse}
.jobs th{font-family:"Roboto Condensed",sans-serif;font-size:8.2px;color:var(--ink);text-align:left;height:24px;border-bottom:2px solid var(--line);font-weight:700;letter-spacing:.2px;position:relative}
.jobs td{font-size:8.2px;height:30.5px;border-bottom:1px solid var(--line);vertical-align:middle;letter-spacing:.1px}
.jobs tr:first-child td{height:36px}

.cta{left:0;top:837px;width:1082px;height:68px;background:var(--lime)}
.cta p{position:absolute;left:211px;top:26px;font-family:"Roboto Condensed",sans-serif;font-size:11.5px;font-weight:700;color:var(--forest-deep)}
.cta a{position:absolute;left:781px;top:20px;width:90px;height:28px;background:var(--forest-deep);color:#fff;font-family:"Roboto Condensed",sans-serif;font-weight:700;font-size:8.5px;letter-spacing:1px;display:flex;align-items:center;justify-content:center;text-decoration:none}

.footer{left:0;top:905px;width:1082px;height:295px;background:var(--footer);color:var(--footer-text);font-size:8.4px}
.finfo{top:32px;display:flex;gap:9px;align-items:center;line-height:13.6px}
.finfo .ico{width:22px;height:22px;border-radius:50%;background:var(--footer-chip);display:flex;align-items:center;justify-content:center}
.fdiv{left:381px;top:79px;width:490px;height:1px;background:var(--footer-line)}
.fabout{left:211px;top:100px;width:145px;line-height:13.6px;letter-spacing:.15px}
.fsocial{left:211px;top:184px;display:flex;gap:5px}
.fsocial span{width:24px;height:24px;border-radius:50%;background:var(--footer-chip);display:flex;align-items:center;justify-content:center}
.fsocial span.on{background:var(--leaf)}
.fsocial i{width:5px;height:5px;border-radius:50%;background:#d2d9d3}
.fcol{top:101px}
.fcol h4{font-family:"Roboto Condensed",sans-serif;color:#e6ece7;font-size:10px;letter-spacing:.3px;margin-bottom:13px}
.fcol ul{list-style:none}
.fcol li{height:23.2px;padding-left:10px;position:relative;letter-spacing:.15px}
.fcol li::before{content:"";position:absolute;left:0;top:4px;width:3px;height:3px;border-radius:50%;background:#69746b}
.fcol li.active{color:#fff}
.fcol li.active::before{background:#fff}
.news p{line-height:13.6px;width:152px}
.news .field{margin-top:14px;width:152px;height:23px;background:#25342a;padding:7px 9px;font-size:7.5px;color:#b7c1b9}
.news .btn{margin-top:7px;width:152px;height:23px;background:var(--leaf);color:#fff;font-family:"Roboto Condensed",sans-serif;font-weight:700;font-size:7px;letter-spacing:.5px;display:flex;align-items:center;justify-content:center}
.fline{left:211px;top:256px;width:660px;height:1px;background:var(--footer-line)}
.copy{left:0;top:271px;width:1082px;text-align:center;font-size:7.5px;color:#5c675e}
</style>
</head>
<body>

<div class="abs topbar">
  <div class="abs contact">
    <span><svg width="8" height="8" viewBox="0 0 8 8"><path d="M1 5V4a3 3 0 0 1 6 0v1M1 5h1.3v2H1zM5.7 5H7v2H5.7z" fill="none" stroke="#b9c3ba" stroke-width=".8"/></svg>(+61) 0400 218 735</span>
    <span>|</span>
    <span><svg width="8" height="8" viewBox="0 0 8 8"><rect x=".5" y="1.5" width="6" height="6" fill="none" stroke="#b9c3ba" stroke-width=".8"/><path d="M3 5l4-4" stroke="#b9c3ba" stroke-width=".8"/></svg>hello@pelhamgrove.co</span>
  </div>
  <div class="abs socials"><span><i></i></span><span><i></i></span><span><i></i></span><span><i></i></span><span><i></i></span></div>
  <div class="abs search">Search...<svg width="8" height="8" viewBox="0 0 8 8"><circle cx="3.4" cy="3.4" r="2.5" fill="none" stroke="#56625a" stroke-width=".9"/><path d="M5.3 5.3L7.5 7.5" stroke="#56625a" stroke-width=".9"/></svg></div>
</div>

<header class="abs header">
  <div class="abs logo"><i></i>PELHAM GROVE</div>
  <nav class="abs nav"><span>HOME</span><span>ABOUT</span><span>SERVICE</span><span>PORTFOLIO</span><span>FEATURES</span><span>CONTACT</span></nav>
  <div class="abs quote">GET A QUOTE</div>
</header>

<div class="abs crumb">Home &nbsp;›&nbsp; <b>Careers</b></div>

<aside>
  <div class="abs side-box">
    <h3>ABOUT US</h3>
    <ul><li>About Us</li><li>Company History</li><li class="current">Careers</li><li>Our Partner</li><li>Leadership</li><li>Contact Us</li></ul>
  </div>
  <div class="abs brochure"><svg width="11" height="13" viewBox="0 0 11 13"><path d="M1 .5h6l3 3v9H1z" fill="none" stroke="#fff" stroke-width="1"/><path d="M3 9c2-4 3-5 5 0" fill="none" stroke="#fff" stroke-width=".8"/></svg>DOWLOAD BROCHURE</div>
  <div class="abs testimonial">
    <h3>TESTIMONIAL</h3>
    <p>" Solar photovoltaic (pv) modules generate electricity from sunlight, which can be fed into the mains electricity supply of a building or sold to the public electricity grid.</p>
  </div>
  <div class="abs author">
    <div class="avatar" role="img" aria-label="Portrait photo of the company chief executive"></div>
    <div><b>Darren Holloway</b><small>C.E.O BRIGHTFIELD CO</small></div>
  </div>
</aside>

<section class="abs intro">
  <h1>We are a strong collective!</h1>
  <p>Photovoltaics were initially solely used as a source of electricity for small and medium-sized applications, from the calculator powered by a single solar cell to remote homes powered by an off-grid rooftop PV system. As the cost of solar electricity has fallen, the number of grid-connected solar PV systems has grown into the millions and utility-scale solar power stations with hundreds.</p>
</section>
<section class="abs cols">
  <div><h2>General Requirements</h2><p>Solar power is the conversion of sunlight into electricity, either directly using photovoltaics (PV), or indirectly using concentrated solar power (CSP). Concentrated solar power systems use lenses or mirrors and tracking systems to focus.</p></div>
  <div><h2>Benefits and Rewards</h2><p>A solar cell, or photovoltaic cell (PV), is a device that converts light into electric current using the photovoltaic effect. The first solar cell was constructed by Charles Fenwick in the 1880s.[4] The German industrialist Ernst Walter Hansel.</p></div>
</section>
<div class="abs photo" role="img" aria-label="Top-down photo of a solar panel, plans, light bulbs and a green plant on a desk"></div>

<div class="abs acc-open">
  <div class="head">What We Can Offer?<span>−</span></div>
  <p>Solar power is the conversion of sunlight into electricity, either directly using photovoltaics (PV), or indirectly using concentrated solar power (CSP). Concentrated solar power systems use lenses or mirrors and tracking systems to focus a large area of sunlight into a small beam. Photovoltaics convert light into an electric current using the photovoltaic effect.</p>
</div>
<div class="abs acc" style="top:533px">What You Will Do?<span>+</span></div>
<div class="abs acc" style="top:566px">Why You'll Love Working Here?<span>+</span></div>

<table class="abs jobs">
  <colgroup><col style="width:171px"><col style="width:113px"><col style="width:114px"><col></colgroup>
  <thead><tr><th>POSITION RECRUITMENT</th><th>DEPARTMENT</th><th>LOCATION</th><th>TIME/NOTED<svg style="position:absolute;right:0;top:9px" width="6" height="4" viewBox="0 0 6 4"><path d="M.5.5l2.5 2.5 2.5-2.5" fill="none" stroke="#1b2a20" stroke-width=".9"/></svg></th></tr></thead>
  <tbody>
    <tr><td>Engineering Project Supervision</td><td>Engineering</td><td>Liverpool, UK</td><td>&nbsp;Completed</td></tr>
    <tr><td>Planned cost estimates</td><td>&nbsp;Accountant</td><td>Quebec, CA</td><td>&nbsp;&nbsp;08, May, 2016</td></tr>
    <tr><td>Maintenance and Repair Manager</td><td>&nbsp;J Manager</td><td>LA, US</td><td>&nbsp;&nbsp;21, August, 2016</td></tr>
    <tr><td>Vice president of engineering</td><td>&nbsp;Leader</td><td>Texas, US</td><td>&nbsp;&nbsp;08, July, 2016</td></tr>
  </tbody>
</table>

<div class="abs cta">
  <p>Contact us at the Pelham Grove office nearest to you or submit a business inquiry online.</p>
  <a>CONTACT US</a>
</div>

<footer class="abs footer">
  <div class="abs finfo" style="left:381px"><span class="ico"><svg width="9" height="10" viewBox="0 0 9 10"><path d="M4.5 9.5S1 6 1 4a3.5 3.5 0 0 1 7 0c0 2-3.5 5.5-3.5 5.5z" fill="none" stroke="#c4cdc6" stroke-width=".9"/><circle cx="4.5" cy="4" r="1.2" fill="none" stroke="#c4cdc6" stroke-width=".9"/></svg></span><span>24 Wattle Street - Orange<br>NSW</span></div>
  <div class="abs finfo" style="left:556px"><span class="ico"><svg width="9" height="9" viewBox="0 0 9 9"><path d="M1.5 7.5c1-3 3-5 6-6M1.5 7.5l1.5.3M7.5 1.5l-.3 1.5" fill="none" stroke="#c4cdc6" stroke-width=".9"/></svg></span><span>(+61) 0400 218 735<br>(02) 6361 4420</span></div>
  <div class="abs finfo" style="left:719px"><span class="ico"><svg width="9" height="7" viewBox="0 0 9 7"><rect x=".5" y=".5" width="8" height="6" fill="none" stroke="#c4cdc6" stroke-width=".9"/><path d="M.5.5l4 3.3 4-3.3" fill="none" stroke="#c4cdc6" stroke-width=".9"/></svg></span><span>info@pelhamgrove.co</span></div>
  <div class="abs fdiv"></div>

  <p class="abs fabout">We are Pelham Grove, we industry factory company and provide you the best service and support comes register to receive service information</p>
  <div class="abs fsocial"><span><i></i></span><span class="on"><i></i></span><span><i></i></span><span><i></i></span></div>

  <div class="abs fcol" style="left:381px"><h4>QUICKLINK</h4><ul><li class="active">Clean Energy</li><li>Solar Power</li><li>Repair Turbine</li><li>Energy Research</li></ul></div>
  <div class="abs fcol" style="left:550px"><h4>CUSTOMER CARE</h4><ul><li>Customer Service</li><li>Warranty Policy</li><li>Installation and Use</li><li>Contact Us</li></ul></div>
  <div class="abs fcol news" style="left:719px"><h4>NEWSLETTER</h4><p>Sign up for our newsletter and follow us on social media</p><div class="field">Your email address ...</div><div class="btn">SUBSCRIBE</div></div>

  <div class="abs fline"></div>
  <div class="abs copy">Copyright © 2008 - 2016 PelhamGrove.co. All Rights Reserved</div>
</footer>

</body>
</html>
```